Hi,

I would like to have a invitation made for a party. exactly like the picture in the link below.

http://pinboardia.example/pin/730215948361027459/

However, Please change the colors into fun/ girly feeling. font can be different and size of the card should be the same

Name of the girl: RINA
What: Bachelorette Party
Where:TOLO Boat
Dubai Coral Quay Sailing Club
When:7th of February 2013

No RSVP required. (so no need to put it)

```html
<!DOCTYPE html>
<html lang="en">
<head>
<meta charset="utf-8">
<title>Rina's Bachelorette Party Invitation</title>
<link rel="stylesheet" href="https://fonts.googleapis.com/css2?family=Ultra&family=Cinzel:wght@400&family=Oswald:wght@300&display=swap">
<style>
  :root {
    --page: #ffffff;
    --sky: #b8d0ea;
    --fold: #9fb6cf;
    --coral: #f07478;
    --sage: #9aa59b;
    --lavender: #e0d8ec;
    --frame: #8f9a92;
    --inner-rule: #8c8494;
    --value-grey: #7f8a82;
    --white: #ffffff;
    --butterfly-white: #eef3fa;
    --butterfly-peach: #fcd9b8;
    --butterfly-lilac: #c9c0e6;
    --swirl-blue: #a9c3e2;
    --swirl-coral: #e79a93;
  }
  html, body {
    margin: 0;
    padding: 0;
    width: 1200px;
    height: 1000px;
    overflow: hidden;
    background: var(--page);
  }
  .invitation { display: block; width: 1200px; height: 1000px; }
  .card-ground { fill: var(--sky); }
  .fold-line { stroke: var(--fold); stroke-width: 1; }
  .headline-name, .big-word {
    font-family: "Ultra", "Rockwell Extra Bold", "Rockwell", serif;
    fill: var(--coral);
  }
  .big-word {
    stroke: var(--white);
    stroke-width: 9;
    stroke-linejoin: round;
    paint-order: stroke;
  }
  .tagline { font-family: "Ultra", "Rockwell Extra Bold", "Rockwell", serif; fill: var(--sage); }
  .details-frame { fill: var(--lavender); stroke: var(--frame); stroke-width: 4; }
  .details-rule { fill: none; stroke: var(--inner-rule); stroke-width: 0.8; }
  .detail-label {
    font-family: "Oswald", sans-serif;
    font-weight: 300;
    font-size: 16px;
    fill: var(--coral);
    text-anchor: middle;
  }
  .detail-value {
    font-family: "Cinzel", serif;
    font-size: 15px;
    fill: var(--value-grey);
    text-anchor: middle;
  }
  .detail-value.name { font-size: 17px; }
  .ornament-white { fill: var(--butterfly-white); opacity: 0.85; }
  .ornament-peach { fill: var(--butterfly-peach); }
  .ornament-lilac { fill: var(--butterfly-lilac); opacity: 0.7; }
  .ornament-faint { fill: var(--swirl-blue); opacity: 0.45; }
  .ornament-coral { fill: var(--swirl-coral); opacity: 0.45; }
</style>
</head>
<body>
<svg class="invitation" viewBox="0 0 1200 1000" xmlns="http://www.w3.org/2000/svg">
  <!-- card base and folds -->
  <rect class="card-ground" x="26" y="259" width="1164" height="484"/>
  <line class="fold-line" x1="413" y1="259" x2="413" y2="743"/>
  <line class="fold-line" x1="802" y1="259" x2="802" y2="743"/>

  <!-- decorative areas, kept clear of the lettering -->
  <rect class="ornament-white" x="28" y="266" width="92" height="70" rx="30" role="img" aria-label="White butterfly with curling antennae"/>
  <rect class="ornament-peach" x="396" y="316" width="58" height="52" rx="22" role="img" aria-label="Peach butterfly"/>
  <rect class="ornament-faint" x="182" y="292" width="72" height="30" rx="14" role="img" aria-label="Faint scroll ornament"/>
  <rect class="ornament-faint" x="492" y="372" width="222" height="40" rx="20" role="img" aria-label="Faint flourish ornament"/>
  <rect class="ornament-faint" x="570" y="698" width="72" height="30" rx="14" role="img" aria-label="Faint scroll ornament"/>
  <rect class="ornament-coral" x="30" y="664" width="154" height="24" rx="12" role="img" aria-label="Coral dotted swirl flourish"/>
  <rect class="ornament-coral" x="386" y="512" width="38" height="120" rx="16" role="img" aria-label="Coral swirl flourish between the letters"/>
  <rect class="ornament-coral" x="540" y="664" width="146" height="24" rx="12" role="img" aria-label="Coral dotted swirl flourish"/>
  <rect class="ornament-white" x="700" y="664" width="36" height="24" rx="10" role="img" aria-label="Small white butterfly"/>
  <rect class="ornament-coral" x="772" y="490" width="24" height="22" rx="9" role="img" aria-label="Small coral butterfly"/>

  <!-- headline -->
  <text class="headline-name" x="58" y="425" font-size="88" textLength="322" lengthAdjust="spacingAndGlyphs">RINA’S</text>
  <text class="tagline" x="56" y="482" font-size="40" textLength="324" lengthAdjust="spacingAndGlyphs">LAST CHANCE TO</text>
  <text class="tagline" x="432" y="482" font-size="40" textLength="356" lengthAdjust="spacingAndGlyphs">CELEBRATE BEING</text>
  <text class="big-word" x="62" y="655" font-size="200" textLength="316" lengthAdjust="spacingAndGlyphs">SIN</text>
  <text class="big-word" x="432" y="655" font-size="200" textLength="354" lengthAdjust="spacingAndGlyphs">GLE</text>

  <!-- details panel -->
  <rect class="details-frame" x="825" y="286" width="341" height="432" rx="9"/>
  <rect class="details-rule" x="836" y="299" width="319" height="407" rx="6"/>
  <rect class="ornament-coral" x="922" y="322" width="140" height="46" rx="20" role="img" aria-label="Coral dotted scroll ornament"/>

  <text class="detail-label" x="993" y="406">WHO</text>
  <text class="detail-value name" x="993" y="428">RINA</text>
  <text class="detail-label" x="993" y="467">WHAT</text>
  <text class="detail-value" x="993" y="486">BACHELORETTE PARTY</text>
  <text class="detail-label" x="993" y="527">WHEN</text>
  <text class="detail-value" x="993" y="548" font-size="13">FEBRUARY 7TH, 2013</text>
  <text class="detail-label" x="993" y="585">WHERE</text>
  <text class="detail-value" x="993" y="605">TOLO BOAT</text>
  <text class="detail-value" x="993" y="622" font-size="14">DUBAI CORAL QUAY SAILING CLUB</text>

  <rect class="ornament-lilac" x="1072" y="634" width="70" height="60" rx="24" role="img" aria-label="Lilac butterfly"/>
</svg>
</body>
</html>
```